Marrowfield Benefit Advisors Business Card Design

I already placed order for cards through sketch hive.

Double sided- back Navy with White logo and raised silver "swoosh"

```html
<!DOCTYPE html>
<html lang="en">
<head>
<meta charset="utf-8">
<title>Marrowfield Benefit Advisors – Business Card</title>
<link rel="stylesheet" href="https://fonts.googleapis.com/css2?family=Montserrat:wght@400;500;700&display=swap">
<style>
  :root {
    --stage: #3a3a3a;
    --card-front: #ffffff;
    --card-back: #141414;
    --navy: #13234a;
    --ink: #3b3b3b;
    --silver: #c9c9c9;
  }
  * { margin: 0; padding: 0; box-sizing: border-box; }
  html, body {
    width: 1200px; height: 1059px; overflow: hidden;
    background: var(--stage);
    font-family: "Montserrat", sans-serif;
  }
  .card {
    position: absolute;
    border-radius: 24px;
  }
  .card--front {
    left: 256px; top: 100px; width: 688px; height: 393px;
    background: var(--card-front);
  }
  .card--back {
    left: 253px; top: 535px; width: 694px; height: 397px;
    background: var(--card-back);
  }
  .brand {
    position: absolute;
    display: flex; align-items: center; gap: 12px;
    font-weight: 700;
  }
  .brand__dot {
    width: 14px; height: 14px; border-radius: 50%;
    background: currentColor; flex: none;
  }
  .brand__name { line-height: 1.1; text-transform: uppercase; }
  .brand__main { display: block; }
  .brand__sub { display: block; letter-spacing: 0.35em; }
  .card--front .brand {
    left: 40px; top: 171px; color: var(--navy);
  }
  .card--front .brand__main { font-size: 27px; letter-spacing: 0.02em; }
  .card--front .brand__sub { font-size: 9.5px; margin-top: 4px; }
  .divider {
    position: absolute; left: 364px; top: 91px;
    width: 2px; height: 213px; background: var(--navy);
  }
  .contact {
    position: absolute; left: 392px; top: 84px;
    color: var(--ink);
  }
  .contact__name {
    font-size: 30px; font-weight: 700; color: var(--navy);
    line-height: 1; letter-spacing: 0.005em;
  }
  .contact__title { font-size: 17.5px; margin-top: 9px; }
  .contact__address { font-size: 17.5px; line-height: 28px; margin-top: 18px; }
  .contact__list { list-style: none; margin-top: 14px; font-size: 17.5px; }
  .contact__list li {
    display: flex; align-items: center; gap: 9px; height: 27.5px;
  }
  .contact__icon { width: 14px; height: 14px; fill: var(--navy); flex: none; }
  .card--back .brand {
    left: 50%; top: 50%; transform: translate(-50%, -50%);
    color: var(--silver); gap: 18px;
  }
  .card--back .brand__dot { width: 22px; height: 22px; }
  .card--back .brand__main { font-size: 50px; letter-spacing: 0.02em; }
  .card--back .brand__sub { font-size: 14px; margin-top: 8px; letter-spacing: 0.55em; }
</style>
</head>
<body>
  <section class="card card--front">
    <div class="brand">
      <span class="brand__dot"></span>
      <span class="brand__name">
        <span class="brand__main">Marrowfield</span>
        <span class="brand__sub">Benefit Advisors</span>
      </span>
    </div>
    <div class="divider"></div>
    <div class="contact">
      <h1 class="contact__name">DANIEL HARTLEY</h1>
      <p class="contact__title">Managing Director</p>
      <p class="contact__address">Your address, City<br>State, Zip 1234</p>
      <ul class="contact__list">
        <li>
          <svg class="contact__icon" viewBox="0 0 16 16"><path d="M1 6c0-2 3-3 7-3s7 1 7 3v1h-3.5V5.5h-7V7H1z"/><path d="M3.5 8h9l1 6h-11z"/></svg>
          123 456 789
        </li>
        <li>
          <svg class="contact__icon" viewBox="0 0 16 16"><path d="M1 3h14v1.5L8 9 1 4.5z"/><path d="M1 6.2 8 10.7l7-4.5V13H1z"/></svg>
          info@yourmailbox.com
        </li>
        <li>
          <svg class="contact__icon" viewBox="0 0 16 16"><circle cx="8" cy="8" r="7"/><path d="M4 5c1.5 0 2 1 3 1s1 2 0 2.5-1 2 0 3M11 3.5c-1 1-.5 2 .5 2.5s1.5 2 .5 3" stroke="#fff" stroke-width="1.2" fill="none"/></svg>
          www.yourwebsite.com
        </li>
      </ul>
    </div>
  </section>

  <section class="card card--back">
    <div class="brand">
      <span class="brand__dot"></span>
      <span class="brand__name">
        <span class="brand__main">Marrowfield</span>
        <span class="brand__sub">Benefit Advisors</span>
      </span>
    </div>
  </section>
</body>
</html>
```